Bright Path Attorneys Billboard Design for Personal Injury Law Firm

Need a billboard design that we can use for different versions. 1400px X 400px jpeg or png
I have attached the logo and the attorney for the billboard. Attorney Marla Benning
Here is a link to our current website brightpathlegalgroup.example

HEADLINE: HIT BY A TRUCK?
SUBHEAD: NO FEE. BIG FIGHT.
877-GRANTLY

HEADLINE: ACCIDENT?
SUBHEAD: NO FEE, UNLESS WE WIN!
877-GRANTLY

HEADLINE: BIG TRUCK. BIG CASE.
SUBHEAD: YOU PAY $0 UPFRONT
877-GRANTLY

Target Market(s)

People in Car Accident

Industry/Entity Type

Personal Injury Attorneys

```html
<!DOCTYPE html>
<html lang="en">
<head>
<meta charset="UTF-8">
<title>Bright Path Attorneys – Accident Billboard</title>
<link rel="stylesheet" href="https://fonts.googleapis.com/css2?family=Archivo:wght@500;700;800&display=swap">
<style>
  :root {
    --page-bg: #eef1f5;
    --board-navy: #141d2c;
    --board-navy-light: #2a3547;
    --accent-green: #5fd23e;
    --text-white: #ffffff;
    --dash-white: rgba(255,255,255,0.85);
    --portrait-dark: #1c2436;
    --portrait-warm: #b58a62;
  }
  * { margin: 0; padding: 0; box-sizing: border-box; }
  html, body {
    width: 1200px;
    height: 1200px;
    overflow: hidden;
    background: var(--page-bg);
    font-family: "Archivo", Arial, sans-serif;
  }
  .billboard {
    position: absolute;
    left: 40px;
    top: 440px;
    width: 1120px;
    height: 320px;
    overflow: hidden;
    background: var(--board-navy);
  }
  .scene-backdrop {
    position: absolute;
    inset: 0;
    background:
      radial-gradient(ellipse 55% 80% at 45% 65%, rgba(90,104,126,0.45), transparent 70%),
      linear-gradient(90deg, var(--board-navy) 0%, var(--board-navy-light) 55%, var(--board-navy) 100%);
  }
  .headline {
    position: absolute;
    left: 29px;
    top: 22px;
    font-size: 88px;
    font-weight: 800;
    line-height: 1;
    color: var(--text-white);
    letter-spacing: 0.5px;
  }
  .subhead {
    position: absolute;
    left: 28px;
    top: 146px;
    font-size: 64px;
    font-weight: 700;
    line-height: 1;
    color: var(--accent-green);
    white-space: nowrap;
  }
  .brand {
    position: absolute;
    left: 30px;
    top: 252px;
    display: flex;
    align-items: center;
    gap: 12px;
  }
  .brand-dot {
    width: 30px;
    height: 30px;
    border-radius: 50%;
    background: var(--accent-green);
  }
  .brand-name {
    font-size: 26px;
    font-weight: 500;
    color: var(--text-white);
    letter-spacing: 0.5px;
  }
  .call-box {
    position: absolute;
    left: 585px;
    top: 19px;
    width: 338px;
    height: 94px;
    border: 2px dashed var(--dash-white);
    border-radius: 10px;
    padding: 12px 14px;
  }
  .call-label {
    font-size: 23px;
    font-weight: 700;
    color: var(--accent-green);
    line-height: 1;
  }
  .call-number {
    display: flex;
    align-items: center;
    gap: 8px;
    margin-top: 10px;
    font-size: 36px;
    font-weight: 700;
    color: var(--text-white);
    line-height: 1;
  }
  .call-number svg { width: 32px; height: 32px; flex: none; }
  .call-connector {
    position: absolute;
    left: 0;
    top: 0;
    width: 1120px;
    height: 320px;
    pointer-events: none;
  }
  .attorney-portrait {
    position: absolute;
    left: 862px;
    top: 0;
    width: 258px;
    height: 320px;
    background:
      radial-gradient(ellipse 45% 35% at 50% 28%, var(--portrait-warm), transparent 75%),
      linear-gradient(180deg, rgba(28,36,54,0) 0%, var(--portrait-dark) 70%);
  }
</style>
</head>
<body>
  <section class="billboard" aria-label="Bright Path Attorneys accident billboard">
    <div class="scene-backdrop" role="img" aria-label="Darkened photo of a damaged car after a collision"></div>

    <h1 class="headline">ACCIDENT?</h1>
    <p class="subhead">NO FEE UNLESS WE WIN!</p>

    <div class="brand">
      <span class="brand-dot"></span>
      <span class="brand-name">BRIGHT PATH ATTORNEYS</span>
    </div>

    <div class="call-box">
      <p class="call-label">CALL ME TODAY</p>
      <p class="call-number">
        <svg viewBox="0 0 24 24" fill="none" stroke="#ffffff" stroke-width="1.6" stroke-linejoin="round" aria-hidden="true">
          <path d="M5 3h4l2 5-2.5 1.5a11 11 0 0 0 6 6L16 13l5 2v4a2 2 0 0 1-2 2A16 16 0 0 1 3 5a2 2 0 0 1 2-2z"/>
          <path d="M15 3a6 6 0 0 1 6 6M15 7a2 2 0 0 1 2 2"/>
        </svg>
        877-GRANTLY
      </p>
    </div>

    <svg class="call-connector" viewBox="0 0 1120 320" aria-hidden="true">
      <path d="M880 113 C 880 140, 840 150, 850 172 C 858 190, 885 178, 872 166 C 862 158, 850 182, 880 196 C 895 202, 905 200, 915 198"
            fill="none" stroke="#ffffff" stroke-width="2" stroke-dasharray="5 5" opacity="0.85"/>
    </svg>

    <div class="attorney-portrait" role="img" aria-label="Portrait of attorney Marla Benning in a navy blazer, arms crossed"></div>
  </section>
</body>
</html>
```